Jägerbrief
Zielgruppe
Es soll ein 'Jägerbrief' werden. Diesen Jägerbrief erhält ein Jäger, wenn er sein erstes Stück Wild auf einer Jagd erlegen konnte.
Aufgabenstellung
Das Design ist im Format einer Urkunde auszuhändigen und sollte gerne in einem traditionellen Design gemacht werden. Beispielbilder sind im Anhang und können gerne als Inspiration genommen werden.
Genaue Details:
Überschrift in groß 'Jägerbrief'
Darunter den Text zentriert wie folgt abbilden:
'Im Revier von Birkenwöhrden, gelegen im Herzen von Wiesmarschen, tratst du,
zur Niederwildjagd an und bewiesest dein Können, deinen Respekt vor der Natur und deine Geduld im Angesicht der Herausforderung.
An diesem besonderen Tag hattest du die Ehre, deinen ersten Feldhasen zu strecken. Mit diesem Erfolg trittst du in die stolze Tradition der Waidmänner ein, die die Schönheit und den Wert unserer heimischen Wildbestände zu schätzen wissen und Verantwortung für deren Erhalt übernehmen.
Möge dieser Moment dir stets in Erinnerung bleiben und dir ein Ansporn sein, die Jagd mit Demut, Leidenschaft und Verantwortung auszuüben.
Mit diesem Jägerbrief gratulieren wir dir herzlich zu deinem ersten Feldhasen und wünschen dir weiterhin Waidmannsheil auf all deinen Wegen im Revier.
Hochachtungsvoll und mit Waidmannsgruß
Die Jagdgesellschaft von Birkenwöhrden'

```html
<!DOCTYPE html>
<html lang="de">
<head>
<meta charset="utf-8">
<title>Jägerbrief</title>
<link rel="stylesheet" href="https://fonts.googleapis.com/css2?family=Mulish:wght@400;800&display=swap">
<style>
  :root {
    --page: #ffffff;
    --ink: #1b1b1b;
    --photo-warm-light: #d9b06a;
    --photo-warm-mid: #9a7440;
    --photo-warm-dark: #4d4a25;
    --photo-grey-light: #c9c6c2;
    --photo-grey-mid: #85817c;
    --photo-grey-dark: #3f3d3a;
    --panel-warm-a: #ddd5cc;
    --panel-warm-b: #c9c1b6;
    --panel-grey-a: #d6d2cf;
    --panel-grey-b: #bfbab6;
    --emblem: #2a2a2a;
  }
  * { box-sizing: border-box; margin: 0; padding: 0; }
  html, body {
    width: 800px; height: 1200px; overflow: hidden;
    background: var(--page);
  }
  .sheet { position: relative; width: 800px; height: 1200px; }

  .certificate {
    position: absolute; left: 70px; width: 674px; height: 476px;
    overflow: hidden;
  }
  .certificate--colour { top: 48px; }
  .certificate--mono { top: 604px; }

  .certificate__photo {
    position: absolute; left: 0; top: 0; width: 334px; height: 100%;
  }
  .certificate--colour .certificate__photo {
    background:
      radial-gradient(circle at 72% 38%, rgba(255,236,190,.85) 0, rgba(255,236,190,0) 30%),
      linear-gradient(180deg, var(--photo-warm-light) 0%, var(--photo-warm-mid) 55%, var(--photo-warm-dark) 100%);
  }
  .certificate--mono .certificate__photo {
    background:
      radial-gradient(circle at 72% 38%, rgba(245,242,238,.85) 0, rgba(245,242,238,0) 30%),
      linear-gradient(180deg, var(--photo-grey-light) 0%, var(--photo-grey-mid) 55%, var(--photo-grey-dark) 100%);
  }

  .certificate__panel {
    position: absolute; left: 334px; top: 0; width: 340px; height: 100%;
    text-align: center; color: var(--ink);
  }
  .certificate--colour .certificate__panel {
    background: linear-gradient(160deg, var(--panel-warm-a), var(--panel-warm-b));
  }
  .certificate--mono .certificate__panel {
    background: linear-gradient(160deg, var(--panel-grey-a), var(--panel-grey-b));
  }

  .certificate__title {
    position: absolute; left: 14px; top: 30px; width: 240px;
    font-family: "Mulish", sans-serif; font-weight: 800;
    font-size: 40px; line-height: 1; text-align: left;
    color: var(--ink);
  }

  .certificate__emblem {
    position: absolute; left: 262px; top: 10px; width: 66px; height: 89px;
    background: var(--emblem); opacity: .18; border-radius: 6px;
  }

  .certificate__text {
    position: absolute; left: 0; width: 100%;
    font-family: "Mulish", sans-serif; font-weight: 400;
    font-size: 9.2px; line-height: 11.6px;
  }
  .certificate__intro { top: 108px; }
  .certificate__name-line {
    position: absolute; left: 56px; top: 164px; width: 226px;
    border-top: 1.4px solid var(--ink);
  }
  .certificate__body { top: 187px; }
  .certificate__body p + p { margin-top: 11.6px; }

  .certificate__closing {
    position: absolute; left: 0; width: 100%;
    font-family: "Mulish", sans-serif; font-weight: 800;
    font-size: 10.4px; line-height: 12px;
  }
  .certificate__greeting { top: 404px; }
  .certificate__signatory { top: 431px; }
</style>
</head>
<body>
<main class="sheet">

  <article class="certificate certificate--colour">
    <div class="certificate__photo" role="img" aria-label="Damhirsch im sonnigen, nebligen Wald auf einer Wiese"></div>
    <section class="certificate__panel">
      <h1 class="certificate__title">Jägerbrief</h1>
      <div class="certificate__emblem" role="img" aria-label="Hirschkopf-Emblem"></div>
      <p class="certificate__text certificate__intro">Im Revier von Birkenwöhrden,<br>gelegen im Herzen von Wiesmarschen, tratst du,</p>
      <div class="certificate__name-line"></div>
      <div class="certificate__text certificate__body">
        <p>zur Niederwildjagd an und bewiesest dein Können,<br>deinen Respekt vor der Natur und deine Geduld im<br>Angesicht der Herausforderung.</p>
        <p>An diesem besonderen Tag hattest du die Ehre,<br>deinen ersten Feldhasen zu strecken.<br>Mit diesem Erfolg trittst du in die stolze Tradition der Waidmänner ein,<br>die die Schönheit und den Wert unserer heimischen Wildbestände<br>zu schätzen wissen und Verantwortung für deren Erhalt übernehmen.</p>
        <p>Möge dieser Moment dir stets in Erinnerung bleiben<br>und dir ein Ansporn sein, die Jagd mit Demut,<br>Leidenschaft und Verantwortung auszuüben.</p>
        <p>Mit diesem Jägerbrief gratulieren wir dir herzlich zu deinem<br>ersten Feldhasen und wünschen dir weiterhin Waidmannsheil<br>auf all deinen Wegen im Revier.</p>
      </div>
      <p class="certificate__closing certificate__greeting">Hochachtungsvoll und mit Waidmannsgruß</p>
      <p class="certificate__closing certificate__signatory">Die Jagdgesellschaft von Birkenwöhrden</p>
    </section>
  </article>

  <article class="certificate certificate--mono">
    <div class="certificate__photo" role="img" aria-label="Damhirsch im nebligen Wald auf einer Wiese, in Grautönen"></div>
    <section class="certificate__panel">
      <h1 class="certificate__title">Jägerbrief</h1>
      <div class="certificate__emblem" role="img" aria-label="Hirschkopf-Emblem"></div>
      <p class="certificate__text certificate__intro">Im Revier von Birkenwöhrden,<br>gelegen im Herzen von Wiesmarschen, tratst du,</p>
      <div class="certificate__name-line"></div>
      <div class="certificate__text certificate__body">
        <p>zur Niederwildjagd an und bewiesest dein Können,<br>deinen Respekt vor der Natur und deine Geduld im<br>Angesicht der Herausforderung.</p>
        <p>An diesem besonderen Tag hattest du die Ehre,<br>deinen ersten Feldhasen zu strecken.<br>Mit diesem Erfolg trittst du in die stolze Tradition der Waidmänner ein,<br>die die Schönheit und den Wert unserer heimischen Wildbestände<br>zu schätzen wissen und Verantwortung für deren Erhalt übernehmen.</p>
        <p>Möge dieser Moment dir stets in Erinnerung bleiben<br>und dir ein Ansporn sein, die Jagd mit Demut,<br>Leidenschaft und Verantwortung auszuüben.</p>
        <p>Mit diesem Jägerbrief gratulieren wir dir herzlich zu deinem<br>ersten Feldhasen und wünschen dir weiterhin Waidmannsheil<br>auf all deinen Wegen im Revier.</p>
      </div>
      <p class="certificate__closing certificate__greeting">Hochachtungsvoll und mit Waidmannsgruß</p>
      <p class="certificate__closing certificate__signatory">Die Jagdgesellschaft von Birkenwöhrden</p>
    </section>
  </article>

</main>
</body>
</html>
```